Medical Marijuana Service in the Bay Area

This is for a business card design that is going to be making medical marijuana deliveries in the bay area. The name of the the business is "Coastal Sage Wellness". I would like to have a modern feel and showing us as a medical marijuana company but at the same time discrete about it. I'm trying to target more sophisticated clients.

Industry/Entity Type

Medical

Contact Information for Business Card

Would like people to know it is for medical marijuana but in a discrete way.

```html
<!DOCTYPE html>
<html lang="en">
<head>
<meta charset="utf-8">
<title>Coastal Sage Wellness – Business Card</title>
<link rel="stylesheet" href="https://fonts.googleapis.com/css2?family=Pacifico&display=swap">
<style>
  :root {
    --backdrop: #333333;
    --card-light: #d4d5d6;
    --card-green: #067a65;
    --brand-green: #0b7f69;
    --accent-red: #d3122f;
    --script: "Pacifico", cursive;
  }
  * { margin: 0; padding: 0; box-sizing: border-box; }
  html, body {
    width: 1018px;
    height: 1200px;
    overflow: hidden;
    background: var(--backdrop);
  }
  .sheet {
    position: relative;
    width: 1018px;
    height: 1200px;
  }
  .card {
    position: absolute;
    left: 27px;
    width: 964px;
    height: 565px;
  }
  .card--front {
    top: 22px;
    background: var(--card-light);
    display: flex;
    align-items: center;
    justify-content: center;
  }
  .card--back {
    top: 610px;
    background: var(--card-green);
  }
  .brand {
    font-family: var(--script);
    color: var(--brand-green);
    font-size: 84px;
    line-height: 104px;
    text-align: center;
    font-weight: 400;
  }
  .brand__line {
    display: block;
    white-space: nowrap;
  }
  .brand__mark {
    display: inline-block;
    width: 24px;
    height: 24px;
    margin-left: 12px;
    vertical-align: 0.12em;
    background: var(--accent-red);
  }
  .contact {
    position: absolute;
    left: 0;
    right: 0;
    bottom: 82px;
    text-align: center;
    font-family: var(--script);
    font-style: normal;
    color: var(--card-light);
    font-size: 28px;
    line-height: 44px;
  }
</style>
</head>
<body>
  <main class="sheet">
    <section class="card card--front" aria-label="Card front">
      <h1 class="brand">
        <span class="brand__line">Coastal</span>
        <span class="brand__line">Sage<span class="brand__mark" aria-hidden="true"></span></span>
        <span class="brand__line">Wellness</span>
      </h1>
    </section>
    <section class="card card--back" aria-label="Card back">
      <address class="contact">
        <p class="contact__phone">phone: 415-555-0142</p>
        <p class="contact__email">email: hello@coastalsagewellness.com</p>
      </address>
    </section>
  </main>
</body>
</html>
```